PSD website for property company

Please read the brief thoroughly.

We are looking for a new website for a property group that does property acquisitions, property development and property management.
They buy, build and lease core inner city industrial assets in Sydney, Australia.
They also invest in residential developments.

Site menu
- Home page
- Property – sub menus include – Leasing ; Projects ; Investments ; Property Management
- Capital and finance
- About
- Contact

They like this website
https://www.vemlor.com.au/

They want the site to be clean, modern and bold.
They like few colors, even black and white is OK to submit

They have a logo and style guide and useable images here:
http://www.kruft.net/temp/PelworWeb2019.zip
The zip file is also attached to this project.
We have supplied some images to give you an idea, but we will also require you to provide at least 3 extra images from stock photos.
Use your imagination.

I am expecting a lot of similar designs, so be aware the photos you choose will be really important.
They want really 3 good stock photos used and supplied without charge.
Please not too generic, I repeat the quality of the photos is important.
You may provide several photos (but not in multiple submissions please) and we will choose the best three to be provided.

The winner will be selected on a single home page design and required to provide;
All photos use in original format without charge
A second ‘standard page’ template design based on the winning home page design

```html
<!DOCTYPE html>
<html lang="en">
<head>
<meta charset="utf-8">
<title>Pelwor – Buy, Build and Lease Property</title>
<link href="https://fonts.googleapis.com/css2?family=Arimo:wght@400;700&family=Roboto+Condensed:wght@700&display=swap" rel="stylesheet">
<style>
:root{
  --green:#4f6a2b;
  --green-soft:#8ea886;
  --ink:#1c1c1c;
  --text:#333333;
  --muted:#555555;
  --dark:#1e1e1e;
  --paper:#ffffff;
  --card:#f7f9fa;
  --line:#dcdfe2;
  --mint:#f4f8ec;
  --footer-text:#b5b5b5;
}
*{box-sizing:border-box;margin:0;padding:0}
html,body{width:1200px;height:3557px;overflow:hidden;background:var(--paper)}
body{font-family:"Arimo",Arial,sans-serif;color:var(--text);position:relative}
.abs{position:absolute}
.display{font-family:"Roboto Condensed","Arial Narrow",sans-serif;font-weight:700;color:var(--ink)}
.btn{position:absolute;display:flex;align-items:center;justify-content:center;background:var(--green);color:#fff;font-weight:700;font-size:11px;letter-spacing:.6px;text-transform:uppercase}

/* hero */
.hero{position:absolute;left:0;top:0;width:1200px;height:720px}
.hero-photo{position:absolute;inset:0;background:linear-gradient(180deg,#c9d8e6 0%,#dfe7ee 30%,#b9b3a6 60%,#6b5544 85%,#4e4032 100%)}
.hero-building{position:absolute;left:480px;top:80px;width:680px;height:640px;background:linear-gradient(160deg,#7a5a45,#4a3528 70%,#3a2b22)}
.hero-trees{position:absolute;left:0;top:430px;width:560px;height:290px;background:linear-gradient(180deg,#6f7a52,#4b5636)}
.hero-cut{position:absolute;left:0;top:0}
.nav-logo{left:93px;top:26px;font-size:24px;letter-spacing:5px;font-weight:700;color:var(--ink)}
.nav{position:absolute;top:30px;left:0;width:1200px;font-size:14.5px;color:var(--ink)}
.nav span{position:absolute}
.flag{position:absolute;left:1036px;top:29px;width:32px;height:18px;background:linear-gradient(135deg,#1f3a8a,#2a4aa0)}
.hero-title{left:92px;top:214px;font-size:60px;line-height:55px;text-transform:uppercase;letter-spacing:.5px}
.hero-sub{left:95px;top:337px;width:460px;font-size:14.5px;line-height:20px;color:#333}
.counter{left:986px;top:558px;color:#fff;font-size:22px}
.counter b{font-size:48px;font-weight:700;font-family:"Roboto Condensed",sans-serif}
.down{position:absolute;left:558px;top:662px;width:84px;height:84px;border-radius:50%;background:var(--green);border:4px solid #fff}

/* intro */
.intro{left:150px;top:812px;width:900px;text-align:center;font-size:24.5px;line-height:35px;color:#2b2b2b}

/* services */
.svc{position:absolute;width:293px;height:294px}
.svc-back{position:absolute;inset:0;transform:rotate(3deg);background:#d9d9d9}
.svc-back.green{background:var(--green-soft)}
.svc-face{position:absolute;inset:0;background:var(--card);border:1px solid var(--line);text-align:center}
.svc-icon{position:absolute;left:93px;top:32px;width:110px;height:80px}
.svc-icon .dot{position:absolute;left:0;top:10px;width:60px;height:60px;border-radius:50%;background:#d6d9d6}
.svc-icon .art{position:absolute;left:28px;top:0;width:74px;height:76px;background:linear-gradient(135deg,#3a3a3a,#222);opacity:.85;border-radius:6px}
.svc-icon.green .dot{background:#cfdcc8}
.svc h3{position:absolute;top:143px;left:0;width:100%;font-weight:400;font-size:17px;color:var(--ink)}
.svc p{position:absolute;top:175px;left:22px;width:249px;font-size:12px;line-height:18px;color:var(--muted)}
.svc .btn{left:90px;top:282px;width:111px;height:29px;font-size:10px}

/* about */
.about-dark{position:absolute;left:0;top:1436px}
.about-title{left:157px;top:1530px;font-size:34px;color:#fff}
.about-text{left:157px;top:1582px;width:340px;font-size:17.5px;line-height:25px;color:#b9b9b9}

/* capital */
.cap-title{left:0;top:2118px;width:1200px;text-align:center;font-size:50px}
.cap-text{left:90px;top:2194px;width:1020px;text-align:center;font-size:20.5px;line-height:28.5px;color:#333}

/* contact */
.mint{position:absolute;left:0;top:2417px;width:1200px;height:737px;background:var(--mint)}
.contact-photo{position:absolute;left:94px;top:2515px;width:505px;height:457px;background:linear-gradient(180deg,#cfd9e2 0%,#e9e6df 25%,#7a5b46 45%,#5a4334 80%,#3f3129 100%)}
.form-card{position:absolute;left:490px;top:2625px;width:618px;height:433px;background:var(--card);border:1px solid var(--line)}
.form-title{left:50px;top:44px;font-size:50px}
.form-sub{left:51px;top:118px;width:470px;font-size:14px;line-height:21px;color:#555}
.field{position:absolute;background:#fff;border:1px solid #dfe2e5;font-size:11.5px;color:#555;padding:10px 16px}

/* footer */
.footer{position:absolute;left:0;top:3154px;width:1200px;height:403px;background:var(--dark);color:var(--footer-text)}
.f-logo{left:93px;top:74px;font-size:24px;letter-spacing:5px;font-weight:700;color:#fff}
.f-about{left:95px;top:127px;width:330px;font-size:12.5px;line-height:22px}
.f-head{font-family:"Roboto Condensed",sans-serif;font-weight:700;font-size:17px;color:#fff;letter-spacing:.3px}
.f-links{left:541px;top:130px;font-size:12.5px;line-height:22px}
.f-item{position:absolute;left:834px;font-size:12.5px;line-height:18px}
.f-item svg{position:absolute;left:0;top:0}
.f-item span{position:absolute;left:31px;top:0;width:250px}
.f-rule{position:absolute;left:94px;top:290px;width:1012px;height:1px;background:#3a3a3a}
.copy{left:0;top:318px;width:1200px;text-align:center;font-size:12.5px;color:#fff}
</style>
</head>
<body>

<!-- hero -->
<section class="hero">
  <div class="hero-photo" role="img" aria-label="Brick apartment building with arched windows among trees under a bright sky"></div>
  <div class="hero-building"></div>
  <div class="hero-trees"></div>
  <svg class="hero-cut" width="1200" height="720" viewBox="0 0 1200 720"><polygon points="0,639 600,704 1200,639 1200,720 0,720" fill="#fff"/></svg>
</section>
<div class="abs nav-logo">PELWOR</div>
<nav class="nav">
  <span style="left:508px">Home</span>
  <span style="left:592px">Property</span>
  <span style="left:693px">Capital and finance</span>
  <span style="left:866px">About</span>
  <span style="left:949px">Contact</span>
  <span style="left:1077px">AUS</span>
</nav>
<div class="flag" role="img" aria-label="Australian flag"></div>
<h1 class="abs display hero-title">Buy, build and lease<br>property here</h1>
<p class="abs hero-sub">Lorem ipsum dolor sit amet, consectetur adipiscing elit. Aliquam a velit a neque commodo imperdiet.</p>
<div class="btn" style="left:94px;top:406px;width:139px;height:37px;font-size:12.5px">Get Started</div>
<div class="abs counter"><b>01</b> / 03</div>
<div class="down">
  <svg width="76" height="76" viewBox="0 0 76 76"><path d="M38 26v24M31 43l7 7 7-7" stroke="#fff" stroke-width="1.8" fill="none"/></svg>
</div>

<!-- intro -->
<p class="abs intro">Nunc vel turpis a est luctus lobortis. Nulla placerat lorem magna, eget posuere turpis rutrum vitae. Integer auctor porttitor dapibus. Suspendisse dapibus ornare egestas. In rutrum eu tortor nec euismod.</p>

<!-- services -->
<div class="svc" style="left:101px;top:1048px">
  <div class="svc-back"></div>
  <div class="svc-face">
    <div class="svc-icon"><div class="dot"></div><div class="art" role="img" aria-label="Line icon of a house with a contract and pen"></div></div>
    <h3>Property Acquisitions</h3>
    <p>Nunc vel turpis a est luctus lobortis. Nulla placerat lorem magna, eget posuere turpis rutrum vitae Integer auctor.</p>
  </div>
  <div class="btn">Know More</div>
</div>
<div class="svc" style="left:450px;top:974px">
  <div class="svc-back green"></div>
  <div class="svc-face">
    <div class="svc-icon green"><div class="dot"></div><div class="art" role="img" aria-label="Line icon of a house inside a gear"></div></div>
    <h3>Property Development</h3>
    <p>Nunc vel turpis a est luctus lobortis. Nulla placerat lorem magna, eget posuere turpis rutrum vitae Integer auctor.</p>
  </div>
  <div class="btn">Know More</div>
</div>
<div class="svc" style="left:801px;top:1048px">
  <div class="svc-back"></div>
  <div class="svc-face">
    <div class="svc-icon"><div class="dot"></div><div class="art" role="img" aria-label="Line icon of a hand holding buildings and a money bag"></div></div>
    <h3>Property Management</h3>
    <p>Nunc vel turpis a est luctus lobortis. Nulla placerat lorem magna, eget posuere turpis rutrum vitae Integer auctor.</p>
  </div>
  <div class="btn">Know More</div>
</div>

<!-- about -->
<svg class="about-dark" width="1200" height="580" viewBox="0 0 1200 580">
  <polygon points="0,0 601,0 601,504 547,504 0,464" fill="var(--dark)"/>
</svg>
<svg class="abs" style="left:547px;top:1504px" width="653" height="508" viewBox="0 0 653 508" role="img" aria-label="Modern pale stone building with arched ground floor and a lawn in front">
  <defs><linearGradient id="aboutPhoto" x1="0" y1="0" x2="0" y2="1">
    <stop offset="0" stop-color="#9fb8d3"/><stop offset=".35" stop-color="#c9c3b8"/><stop offset=".7" stop-color="#9d8f7c"/><stop offset="1" stop-color="#6f7550"/>
  </linearGradient></defs>
  <polygon points="0,0 653,0 653,464 0,508" fill="url(#aboutPhoto)"/>
</svg>
<h2 class="abs display about-title">About Us</h2>
<p class="abs about-text">Cras vitae dui massa. Phasellus aliquam justo nec efficitur viverra. Nam ullamcorper urna vel neque consectetur, ac auctor lacus gravida. Donec blandit eu sem et molestie. Nullam ut augue quis dolor luctus placerat. Suspendisse potenti.</p>
<div class="btn" style="left:157px;top:1772px;width:112px;height:29px;font-size:10px">Know More</div>

<!-- capital -->
<h2 class="abs display cap-title">Capital And Finance</h2>
<p class="abs cap-text">Nunc vel turpis a est luctus lobortis. Nulla placerat lorem magna, eget posuere turpis rutrum vitae. Integer auctor porttitor dapibus. Suspendisse dapibus ornare egestas. In rutrum eu tortor nec euismod. Donec ut augue at ante sollicitudin ultrices a ut mauris.</p>
<div class="btn" style="left:529px;top:2303px;width:142px;height:38px;font-size:13px">Know More</div>

<!-- contact -->
<div class="mint"></div>
<div class="contact-photo" role="img" aria-label="Brick building facade with tall arched windows and shopfronts at street level"></div>
<div class="form-card">
  <h2 class="abs display form-title">Get In Touch</h2>
  <p class="abs form-sub">Lorem ipsum dolor sit amet, consectetur adipiscing elit. Aliquam a velit a neque commodo imperdiet Aliquam ante est.</p>
  <div class="field" style="left:51px;top:172px;width:254px;height:33px">Your First Name</div>
  <div class="field" style="left:310px;top:172px;width:254px;height:33px">Your Last Name</div>
  <div class="field" style="left:51px;top:212px;width:254px;height:33px">Your Email Id</div>
  <div class="field" style="left:310px;top:212px;width:254px;height:33px">Phone No.</div>
  <div class="field" style="left:51px;top:252px;width:513px;height:83px">Message</div>
  <div class="btn" style="left:51px;top:348px;width:112px;height:29px;font-size:10px">Submit Now</div>
</div>

<!-- footer -->
<footer class="footer">
  <div class="abs f-logo">PELWOR</div>
  <p class="abs f-about">Lorem ipsum dolor sit amet, consectetur adipiscing elit. Aliquam a velit a neque commodo imperdiet. Aliquam ante est, facilisis imperdiet congue aliquet, porta eu ex. Nullam maximus ultrices ultricies.</p>
  <div class="abs f-head" style="left:541px;top:82px">QUICK LINK</div>
  <div class="abs f-links">- Home<br>- Property<br>- Capital and finance<br>- About<br>- Contact</div>
  <div class="abs f-head" style="left:834px;top:82px">QUICK CONTACT</div>
  <div class="f-item" style="top:128px">
    <svg width="16" height="20" viewBox="0 0 16 20"><path d="M8 1a6 6 0 0 0-6 6c0 4.5 6 12 6 12s6-7.5 6-12a6 6 0 0 0-6-6z" fill="#fff"/><circle cx="8" cy="7" r="2.3" fill="var(--dark)"/></svg>
    <span>orem ipsum dolor sit amet, consectetur adipiscing elit. Sydney, Australia</span>
  </div>
  <div class="f-item" style="top:180px">
    <svg width="16" height="16" viewBox="0 0 16 16"><path d="M3 1l3 .5 1 3.5-2 1.5a9 9 0 0 0 4.5 4.5l1.5-2 3.5 1 .5 3-2 2C7 15 1 9 1 3z" fill="#fff"/></svg>
    <span>123 4567 890</span>
  </div>
  <div class="f-item" style="top:215px">
    <svg width="17" height="17" viewBox="0 0 17 17"><circle cx="8.5" cy="8.5" r="7" fill="none" stroke="#fff" stroke-width="1.6"/><circle cx="8.5" cy="8.5" r="2.8" fill="none" stroke="#fff" stroke-width="1.6"/><path d="M11.3 6v3.5c0 1.5 2.3 1.5 2.3 0" fill="none" stroke="#fff" stroke-width="1.6"/></svg>
    <span>info@pelwor.com</span>
  </div>
  <div class="f-rule"></div>
  <div class="abs copy">Copyright © Pelwor 2019 All rights reserved</div>
</footer>

</body>
</html>
```